Store Front Window Design

We have a beautiful corner store front dental practice with no window signage. Crazy I know...that's why we need your help.

The final design will be done in all vinyl unless unless you suggest a different medium (meaning we are open to some design idea like using frosted glass, etc...).

The windows provide a lot of natural light so the design needs to keep a lot of natural light coming into the office. Keep in mind vinyl is not opaque so keep the signage aesthetically pleasing and a minimalist design to allow as much natural light in as possible. The design should follow the aesthetic from our logo. or tie into at least. We want a cohesive brand aesthetic.

I submitted some general layout ideas. There is a blue banner with advertising words which we want to be used in the final version. Even though the lettering is black, in reality the letters will be a white vinyl on the outside of the window. When you submit your work, be sure to add any special instructions (aka tell me the vision for the letters is white not black, maybe gold leaf, or forested glass...stuff like that). AND YOU DO NOT HAVE TO FOLLOW MY PATTERN! YOU ARE ARTISTS AND WE ARE LOOKING FOR AN ARTISTIC EYE CATCHING PRESENTATION OF THIS INFORMATION. MAKE IT FLASHY AND ADD SOME AESTHETIC FROM THE TOOTH LOGO.

The store front is 6 windows roughly 60'' x 36'' The smaller windows below are 27'' x 36''. Around the corner there are 3 windows. they are 60'' x 27'' lower windows are 27" x 27". We would like to keep the bottom windows clear and keep the signage on the top windows, however, we are flexible.

The front 6 windows need to have this information worked into the design.

Practice name: Venn and Obradovic Dental & Orthodontics.
Phone numbers: Maren Venn DDS: 555.218.7043
Piotr Obradovic DDS:555.731.0962

Expertise: Dr. Venn General Dentistry & Orthodontics
Dr. Obradovic Oral Surgery & Sedation

Address: 4819 Thistle Rd

A banner across the bottom of the top windows with some key advertisement words: "Clearvetta" "Braces" "Implants" "Whiting" "Call today" "Free Consultation" "Oral Surgery" "Sedation". We like the two color idea. Its up to you to decide on the color combo. I used a Dark and light blue, but maybe a Blue and grey would nice to tire in the logo colors?

I have made some mock ideas to get the ball rolling but you do not have to stick to these designs at all, just as long as all the required information is there. Be creative with the layouts, fonts, color scheme, (just remember these are going on windows not necessarily a white background), and graphics/artistic flare (refer to logo for layout inspiration and use the logo as an actual graphic). We are running a miltimillion dollar dental practice so we want these windows to be eye catching to pull in patients and look like a million dollar design. Also all 6 windows dont need ot be used. I am really looking for creative design marketing.

The corner 3 windows need the following information: name, expertise, phone number, banner.

Dr. Venn, General Dentistry & Orthodontics, 555.218.7043
Dr. Obradovic, Oral Surgery & Sedation, 555.731.0962

There is also a front door that needs to be designed. The door is 60'' x 36'' (standard door size) We want simple white vinyl on the outside of the door. We need you to organize the information on the door, pick a easy to read font, maybe use the logo and use some of the front window signage aesthetic? Its up to you...but we we were initially thinking of just making the litters white and keep it simple but again you are the designers.

Practice name: Venn and Obradovic General Dentistry & Orthodontics

Address: 4819 Thistle Rd

Phone numbers: Dr. Venn 555.218.7043
Dr. Obradovic 555.731.0962

Hours of operation: Mon: call for an appointment
Tues-Thurs: 9am-5pm
Sat: call for an appointment
Sun: Closed

A line saying we speak Spanish: Se Habla Espanol

*****************************************************************************************************
here are some design that we liked and some rough sketches I made to start the ball rolling. Keep in mind that there are 9 windows for the front because its a corner office, but not all of them have to have stuff on it. We want simple, streamline, classy high commanding price point aesthetic. I am hiring you for your artistic minds.

Target Market(s)

anyone who has dental needs

Industry/Entity Type

Dental

Font styles to use
Serif
Sans Serif

Colors

Designer to choose colors to be used in the design.

Requirements
Must have
• 1. The required information (see project description)
• 2. Logo
• 3. Advertisement banner running along the bottom of all 9 windows (6 in front and 3 on the side)
• NOTE: Look at pictures of the store to get a sense of the customers point of view and also as a reference to how your design will be broken up across several windows or maybe you design something special for every window. But we want the banner to run along all the windows to lead customs to the door on the side. Finally the letters will be done in white vinyl unless state otherwise, remember the window needs to let in natural light so the entire window can not be covered in vinyl.
Nice to have
• artistic flare yet simple and sleep and expensive looking aesthetic. work logo into the design.
Should not have
• The goal is to catch someone eye and give them important information about the practice.
• It should not just be words.
• It should not have to many words
• It must be readable font for cards driving by.

```html
<!DOCTYPE html>
<html lang="en">
<head>
<meta charset="utf-8">
<title>Venn and Obradovic – Window Panel</title>
<link href="https://fonts.googleapis.com/css2?family=Montserrat:wght@400;500;700&family=Barlow+Condensed:wght@700&display=swap" rel="stylesheet">
<style>
  :root {
    --backdrop: #ededed;
    --panel: #333333;
    --ink-light: #ffffff;
    --ink-dark: #333333;
    --rule: #e6e6e6;
  }
  html, body {
    margin: 0;
    padding: 0;
    width: 1200px;
    height: 1200px;
    overflow: hidden;
    background: var(--backdrop);
  }
  .canvas {
    position: relative;
    width: 1200px;
    height: 1200px;
    background: var(--backdrop);
  }
  .panel {
    position: absolute;
    left: 237px;
    top: 0;
    width: 723px;
    height: 1200px;
    background: var(--panel);
    color: var(--ink-light);
    font-family: "Montserrat", sans-serif;
  }
  .line {
    position: absolute;
    left: 0;
    width: 100%;
    text-align: center;
    white-space: nowrap;
    line-height: 1;
  }
  .brand-mark {
    position: absolute;
    left: 311px;
    top: 78px;
    width: 100px;
    height: 100px;
    border: 3px solid var(--ink-light);
    border-radius: 50%;
    box-sizing: border-box;
  }
  .brand-name {
    top: 205px;
    font-weight: 400;
    font-size: 15px;
    letter-spacing: 5.5px;
    padding-left: 5px;
  }
  .brand-sub {
    top: 225px;
    font-weight: 400;
    font-size: 22.5px;
    letter-spacing: 0.5px;
  }
  .doctor-name {
    top: 314px;
    font-weight: 700;
    font-size: 59px;
    letter-spacing: 1px;
  }
  .doctor-title {
    top: 386px;
    font-weight: 700;
    font-size: 59px;
    letter-spacing: 1px;
  }
  .rule {
    position: absolute;
    left: 81px;
    width: 558px;
    height: 5px;
    border-top: 1.5px solid var(--rule);
    border-bottom: 1.5px solid var(--rule);
  }
  .rule-top { top: 485px; }
  .rule-bottom { top: 744px; }
  .specialty {
    font-weight: 500;
    font-size: 43px;
  }
  .specialty-one { top: 540px; }
  .specialty-amp { top: 604px; font-size: 36px; }
  .specialty-two { top: 653px; }
  .phone-row {
    position: absolute;
    top: 796px;
    left: 0;
    width: 100%;
    display: flex;
    justify-content: center;
    align-items: center;
    gap: 18px;
  }
  .phone-icon { width: 74px; height: 74px; }
  .phone-area {
    font-weight: 700;
    font-size: 92px;
    line-height: 1;
    letter-spacing: 2px;
  }
  .phone-number {
    top: 888px;
    font-weight: 700;
    font-size: 92px;
    letter-spacing: 4px;
  }
  .cta-band {
    position: absolute;
    left: 0;
    top: 1018px;
    width: 100%;
    height: 160px;
    background: var(--ink-light);
  }
  .cta-text {
    position: absolute;
    left: 0;
    top: 42px;
    width: 100%;
    text-align: center;
    font-family: "Barlow Condensed", sans-serif;
    font-weight: 700;
    font-size: 76px;
    line-height: 1;
    letter-spacing: 27px;
    padding-left: 20px;
    box-sizing: border-box;
    color: var(--ink-dark);
  }
</style>
</head>
<body>
<main class="canvas">
  <section class="panel">
    <div class="brand-mark" aria-hidden="true"></div>
    <div class="line brand-name">VENN AND OBRADOVIC</div>
    <div class="line brand-sub">DENTAL &amp; ORTHODONTICS</div>

    <h1 class="line doctor-name" style="margin:0">MAREN VENN</h1>
    <div class="line doctor-title">D.D.S.</div>

    <div class="rule rule-top"></div>
    <div class="line specialty specialty-one">General Dentistry</div>
    <div class="line specialty specialty-amp">&amp;</div>
    <div class="line specialty specialty-two">Orthodontics</div>
    <div class="rule rule-bottom"></div>

    <div class="phone-row">
      <svg class="phone-icon" viewBox="0 0 74 74" aria-hidden="true">
        <circle cx="37" cy="37" r="34" fill="none" stroke="#ffffff" stroke-width="3"/>
        <path d="M30 18 C22 22 20 32 24 42 C28 52 36 58 44 57 L47 50 L40 45 L36 48 C32 44 30 38 30 32 L35 29 L34 20 Z" fill="#ffffff"/>
      </svg>
      <span class="phone-area">(555)</span>
    </div>
    <div class="line phone-number">218-7043</div>

    <div class="cta-band">
      <div class="cta-text">CALL FOR A</div>
    </div>
  </section>
</main>
</body>
</html>
```